Emergency Medical Training and Events Company Business Needs Business Card Design

We are in need of a business card for our dynamic company expanding its customer base and need to be easily contacted and identified for when we visit with government officials, potential EMS / Fire agencies and county coordinators to arrange for training programs for first responders to better prepare them for critical thinking at critical incidents.

Target Market(s)

EMS/Fire and Event Promoters

Industry/Entity Type

Medical

Contact Information for Business Card

Two cards, comparable designs:

Martin K. Halvey, Principal, m.halvey@rvqtlo.com
Owen Tash, Event and Training Specialist, o.tash@rvqtlo.com

Font styles to use
Other font styles liked:
• Cambria

Colors

Designer to choose colors to be used in the design.

Requirements
Must have
• Company Logo, Spots for Name, Title, Phone Number, Email, Website
• A bullet list stating that we offer, QRB CPR and First Aid Instructors, Hold the Line Instructors, Event EMS, CME's, MCI Training and Planning. We prefer to have a black background for the card but if you can make a blue or white card stand out we would review that as well.
Should not have
• Tacky logos or special sayings ... simple, elegant, professional is the look we seek

```html
<!DOCTYPE html>
<html lang="en">
<head>
<meta charset="utf-8">
<title>RVQTLO Response – Business Cards</title>
<link rel="stylesheet" href="https://fonts.googleapis.com/css2?family=Open+Sans:wght@400;600;700&display=swap">
<style>
  :root {
    --navy: #0b1a52;
    --red: #c81d20;
    --red-dark: #7d1012;
    --white: #ffffff;
    --stage: #3a3c3f;
    --stage-light: #5b5e62;
    --faint: #f1f2f7;
  }
  * { box-sizing: border-box; margin: 0; padding: 0; }
  html, body { width: 1200px; height: 900px; overflow: hidden; }
  body {
    background: radial-gradient(ellipse at 60% 40%, var(--stage-light), var(--stage) 70%);
    font-family: "Open Sans", Arial, sans-serif;
    position: relative;
  }
  .card {
    position: absolute;
    left: 280px;
    width: 640px;
    height: 366px;
    border-radius: 18px;
    overflow: hidden;
    background: var(--white);
    box-shadow: 0 14px 30px rgba(0,0,0,.45);
  }
  .card--brand { top: 40px; }
  .card--contact { top: 470px; }
  .card__art { position: absolute; inset: 0; width: 100%; height: 100%; }

  .brand-mark {
    position: absolute;
    display: flex;
    align-items: center;
    gap: 10px;
    color: var(--white);
    font-weight: 700;
    font-size: 22px;
    letter-spacing: .5px;
    white-space: nowrap;
  }
  .brand-mark__dot {
    flex: none;
    width: 36px; height: 36px;
    border-radius: 50%;
    background: var(--white);
  }
  .card--brand .brand-mark { left: 50px; top: 140px; }
  .card--contact .brand-mark { left: 362px; top: 92px; }

  .band-url {
    position: absolute;
    color: var(--white);
    font-size: 16px;
    letter-spacing: .5px;
    display: flex;
    align-items: center;
    gap: 14px;
    white-space: nowrap;
  }
  .card--brand .band-url { left: 140px; top: 271px; }
  .card--contact .band-url { left: 50px; top: 270px; }
  .band-url__icon {
    width: 26px; height: 26px;
    background: var(--white);
    border-radius: 4px;
    display: flex; align-items: center; justify-content: center;
  }

  .person { position: absolute; left: 50px; top: 62px; }
  .person__name {
    color: var(--navy);
    font-weight: 700;
    font-size: 26px;
    letter-spacing: .5px;
  }
  .person__title {
    color: var(--red);
    font-size: 13px;
    letter-spacing: .3px;
    margin-top: 2px;
  }
  .person__rule {
    width: 40px; height: 3px;
    background: var(--red);
    margin-top: 10px;
  }
  .contact-list {
    position: absolute;
    left: 50px; top: 148px;
    list-style: none;
  }
  .contact-list__item {
    display: flex; align-items: center; gap: 14px;
    color: var(--navy);
    font-size: 16px;
    margin-bottom: 10px;
  }
  .contact-list__icon {
    width: 24px; height: 24px;
    background: var(--navy);
    border-radius: 4px;
    display: flex; align-items: center; justify-content: center;
  }
</style>
</head>
<body>

<section class="card card--brand" aria-label="Card front">
  <svg class="card__art" viewBox="0 0 640 366" aria-hidden="true">
    <circle cx="505" cy="125" r="85" fill="var(--faint)"/>
    <polygon points="0,0 210,0 560,366 0,366" fill="var(--navy)"/>
    <polygon points="175,0 212,0 205,55" fill="var(--red)"/>
    <polygon points="440,250 470,240 470,252 440,262" fill="var(--red-dark)"/>
    <polygon points="0,262 440,262 470,252 470,294 0,306" fill="var(--red)"/>
  </svg>
  <div class="brand-mark"><span class="brand-mark__dot"></span>RVQTLO Response</div>
  <div class="band-url">www.rvqtlo.com</div>
</section>

<section class="card card--contact" aria-label="Card back">
  <svg class="card__art" viewBox="0 0 640 366" aria-hidden="true">
    <polygon points="240,0 640,0 640,262 470,262" fill="var(--navy)"/>
    <polygon points="212,0 246,0 246,52" fill="var(--red)"/>
    <polygon points="470,250 500,240 500,252 470,262" fill="var(--red-dark)"/>
    <polygon points="0,262 470,262 500,252 500,294 0,306" fill="var(--red)"/>
  </svg>
  <div class="brand-mark"><span class="brand-mark__dot"></span>RVQTLO Response</div>

  <div class="person">
    <div class="person__name">OWEN TASH</div>
    <div class="person__title">EVENT AND TRAINING SPECIALIST</div>
    <div class="person__rule"></div>
  </div>

  <ul class="contact-list">
    <li class="contact-list__item">
      <span class="contact-list__icon"><svg width="12" height="16" viewBox="0 0 12 16"><rect x="1" y="1" width="10" height="14" rx="2" fill="none" stroke="#fff" stroke-width="1.6"/><circle cx="6" cy="12.5" r="1" fill="#fff"/></svg></span>
      555.014.2290
    </li>
    <li class="contact-list__item">
      <span class="contact-list__icon"><svg width="14" height="14" viewBox="0 0 14 14"><path d="M3 1l2.5 3-1.5 1.5c.8 1.8 2.2 3.2 4 4L9.5 8l3 2.5-1.5 2.5C6 13 1 8 1 2.5z" fill="#fff"/></svg></span>
      555.017.3846
    </li>
    <li class="contact-list__item">
      <span class="contact-list__icon"><svg width="14" height="10" viewBox="0 0 14 10"><rect x="0.8" y="0.8" width="12.4" height="8.4" fill="none" stroke="#fff" stroke-width="1.4"/><path d="M1 1l6 5 6-5" fill="none" stroke="#fff" stroke-width="1.4"/></svg></span>
      o.tash@rvqtlo.com
    </li>
  </ul>

  <div class="band-url">
    <span class="band-url__icon"><svg width="16" height="14" viewBox="0 0 16 14"><path d="M8 1L1 7h2v6h4V9h2v4h4V7h2z" fill="var(--red)"/></svg></span>
    www.rvqtlo.com
  </div>
</section>

</body>
</html>
```